A Medical Institute that offers treatment for the severely depressed

We need a WEB design for The Brightvale Clinic based in south Florida. We offer a medical treatment that helps severely depressed people, This treatment is only available in a few places around the world. We want a classy design, that compliments our logo. The site will have the home page which will talk briefly about ketamine treatments and our center, a page describing ketamine for the treatment of depression, a page describing the treatment in detail, an about us page, and a FAQ page. The people looking at this site are in a lot of distress, or have a family member who is, and they are looking for hope that they will be able to lead a normal life with this treatment. They have tried everything else out there and nothing has helped, they are desperate for an alternative.

Target Market(s)

People suffering from depression that are researching treatment options on the WEB and specifically ketamine treatments

Industry/Entity Type

Medical

Number of Pages Required

5+ page

Requirements
Must have
• I am not set on any particular design or content. While I personally love color, I don't see it for this project given the attached logo.
Should not have
• sound, a lot of flash, I don't want the site to be difficult to load. I do not want to see the old design of a bar down the side and a graphic across the top, I can do that myself.

```html
<!DOCTYPE html>
<html lang="en">
<head>
<meta charset="utf-8">
<title>The Brightvale Clinic – Ketamine Treatments for Depression</title>
<link rel="stylesheet" href="https://fonts.googleapis.com/css2?family=Open+Sans:wght@400;600&display=swap">
<style>
:root{
  --brown:#6b3a22;
  --brown-dark:#5a2f1a;
  --nav-top:#a8694a;
  --nav-bottom:#7a4328;
  --nav-active:#b98466;
  --text:#1c1c1c;
  --muted:#666;
  --accent-red:#9b1c1c;
  --panel:#ffffff;
  --page-bg:#f1f1f1;
  --form-bg:#e6e6e6;
  --rule:#cfcfcf;
  --gold:#e0b72c;
}
*{margin:0;padding:0;box-sizing:border-box}
html,body{width:1200px;height:1052px;overflow:hidden}
body{position:relative;font-family:'Open Sans',Arial,sans-serif;color:var(--text);
  background:linear-gradient(#e6e6e6 158px,#ececec 500px,#f4f4f4 1052px)}
.abs{position:absolute}

.site-header{position:absolute;left:0;top:0;width:1200px;height:111px;background:#fff}
.brand{left:99px;top:36px;display:flex;align-items:center;gap:10px}
.brand-mark{width:30px;height:30px;background:var(--gold)}
.brand-name{font-size:22px;font-weight:600;color:var(--brown);letter-spacing:.2px}
.contact-line{right:142px;top:36px;text-align:right}
.contact-line .address{font-size:11px;line-height:15px;color:#222}
.contact-line .phone{font-size:19px;line-height:24px;color:#222}
.phone-icon{left:1065px;top:39px;width:34px;height:34px}

.main-nav{position:absolute;left:0;top:111px;width:1200px;height:47px;
  background:linear-gradient(var(--nav-top),var(--nav-bottom))}
.main-nav ul{list-style:none;position:absolute;left:99px;top:0;height:47px;display:flex}
.main-nav li{height:47px;border-left:1px solid rgba(70,30,12,.55);display:flex;align-items:center;justify-content:center;
  font-size:12.5px;color:#f3e4da;text-transform:uppercase}
.main-nav li:last-child{border-right:1px solid rgba(70,30,12,.55)}
.main-nav li.active{background:linear-gradient(#c4957a,#a06c50);color:#fff}

.content-panel{left:99px;top:158px;width:1002px;height:788px;background:var(--panel);
  box-shadow:0 6px 6px -4px rgba(0,0,0,.25)}

.hero{left:111px;top:172px;width:977px;height:356px;
  background:linear-gradient(90deg,#d9d8d6 0%,#d9d8d6 36%,#c7ad8f 55%,#b58e6a 70%,#d8d2c8 100%)}
.hero-title{left:165px;top:283px;width:300px;font-size:22px;line-height:29px;color:#333}
.btn-more{left:167px;top:351px;width:83px;height:34px;background:#fff;border-radius:2px;
  font-size:11px;color:#666;display:flex;align-items:center;justify-content:center}
.slide-arrow{top:419px;width:22px;height:29px}
.slide-prev{left:166px;background:#333}
.slide-next{left:192px;background:#8a8a8a}

.section-title{font-size:26px;line-height:32px;color:var(--brown);font-weight:400}
.welcome{left:113px;top:551px}
.subhead{left:113px;top:593px;font-size:16px;line-height:22px}
.intro{left:114px;top:620px;width:728px;font-size:11.6px;line-height:19px;color:var(--muted)}
.quote{left:114px;top:705px;font-size:11.6px;line-height:19px;color:var(--muted)}
.cta{left:114px;top:729px;font-size:15.5px;line-height:22px}
.cta em{font-style:normal;color:var(--accent-red)}
.rule{left:113px;top:769px;width:725px;height:1px;background:var(--rule)}
.faq-title{left:113px;top:784px}
.faq-next{left:823px;top:794px;width:15px;height:15px}
.question{left:113px;top:825px;font-size:16px;line-height:22px}
.answer{left:114px;top:851px;width:728px;font-size:11.6px;line-height:19px;color:var(--muted)}

.contact-title{left:863px;top:551px}
.contact-form{left:861px;top:597px;width:226px;height:327px;background:var(--form-bg)}
.field{position:absolute;left:9px;width:208px;height:34px;background:#fff;font-size:11px;color:#555;padding:9px 13px}
.field.message{height:86px}
.btn-submit{position:absolute;left:9px;top:282px;width:66px;height:35px;background:var(--brown-dark);
  color:#fff;font-size:11px;display:flex;align-items:center;justify-content:center}

.footer-links{left:99px;top:983px;font-size:11.5px;line-height:18px;color:#222;word-spacing:1px}
.footer-links span{margin:0 9px}
.copyright{left:99px;top:1010px;font-size:11.5px;line-height:18px;color:#222}
.social{top:993px;width:26px;height:26px;border-radius:50%}
.social.s1{left:999px;background:#2f4a8a}
.social.s2{left:1036px;background:#2ea6e6}
.social.s3{left:1074px;background:#1f6fa5}
</style>
</head>
<body>

<header class="site-header">
  <div class="abs brand">
    <div class="brand-mark"></div>
    <div class="brand-name">The Brightvale Clinic</div>
  </div>
  <div class="abs contact-line">
    <div class="address">55 Building name, Street name, City - Zipcode</div>
    <div class="phone">555 240 7183</div>
  </div>
  <svg class="abs phone-icon" viewBox="0 0 34 34" aria-label="Phone">
    <circle cx="17" cy="17" r="16.3" fill="#fff" stroke="#777" stroke-width="1"/>
    <path d="M12.5 10.5c.8-.6 1.6-.5 2 .2l1.3 2.2c.4.7.2 1.3-.4 1.7l-.8.5c.6 1.7 1.8 3 3.4 3.8l.6-.8c.4-.6 1.1-.7 1.7-.3l2.2 1.4c.7.4.8 1.2.2 1.9l-.8 1c-.7.8-2 .9-3.2.3-3.2-1.6-5.5-4.1-6.8-7.4-.4-1.1-.2-2.3.6-3z" fill="#444"/>
  </svg>
</header>

<nav class="main-nav">
  <ul>
    <li class="active" style="width:149px">Home</li>
    <li style="width:272px">Ketamine Description</li>
    <li style="width:180px">About Us</li>
    <li style="width:268px">The Ketamine Therapy</li>
    <li style="width:132px">FAQ</li>
  </ul>
</nav>

<main>
  <div class="abs content-panel"></div>

  <div class="abs hero" role="img" aria-label="Photo of a distressed woman resting her head on her arm"></div>
  <h2 class="abs hero-title" style="font-weight:400">Donec aliquam quam eget euismod dictum</h2>
  <div class="abs btn-more">Read more</div>
  <svg class="abs slide-arrow slide-prev" viewBox="0 0 22 29"><path d="M14 7l-6 7.5 6 7.5" fill="none" stroke="#fff" stroke-width="1.3"/></svg>
  <svg class="abs slide-arrow slide-next" viewBox="0 0 22 29"><path d="M8 7l6 7.5-6 7.5" fill="none" stroke="#fff" stroke-width="1.3"/></svg>

  <h1 class="abs section-title welcome">Welcome to The Brightvale Clinic</h1>
  <h3 class="abs subhead" style="font-weight:400">Ketamine Treatments for Depression</h3>
  <p class="abs intro">Are you or someone you love suffering from depression?&nbsp; Have you had thoughts of suicide?&nbsp; Have you tried medications&nbsp; and nothing is working?&nbsp; Do you feel&nbsp; hopeless?&nbsp; A new treatment offers hope for those people who are suffering from depression and are desperate to get their life back.&nbsp; Ketamine has been used for years as a drug for anesthesia, but administered in small doses, it is extremely effective in treating patients with depression.</p>
  <p class="abs quote">“After suffering with depression for 17 years, I finally feel normal again” say Daniel, after receiving just one ketamine treatment.</p>
  <p class="abs cta"><em>Call us today</em> to find out if ketamine therapy is right for you.</p>
  <div class="abs rule"></div>

  <h2 class="abs section-title faq-title">FAQs</h2>
  <svg class="abs faq-next" viewBox="0 0 15 15"><circle cx="7.5" cy="7.5" r="7.5" fill="#bdbdbd"/><path d="M6 4.5l3.5 3-3.5 3z" fill="#fff"/></svg>
  <h3 class="abs question" style="font-weight:400">Question : Pellentesque vehicula nulla molestie lectus fermentum, id egestas velit aliquet?</h3>
  <p class="abs answer">Answer :<br>Etiam consequat lacus a felis viverra, eget rhoncus massa ullamcorper. Sed quis tincidunt neque. Mauris tellus metus, commodo at quam et, fringilla ullamcorper nisl. Vivamus augue tellus, tincidunt at massa quis, tincidunt cursus nunc. Aliquam pulvinar nulla in arcu condimentum, consequat aliquet nulla euismod.</p>

  <h2 class="abs section-title contact-title">Contact us</h2>
  <form class="abs contact-form">
    <div class="field" style="top:9px">Name</div>
    <div class="field" style="top:52px">E-mail</div>
    <div class="field" style="top:95px">Phone</div>
    <div class="field" style="top:138px">City</div>
    <div class="field message" style="top:187px">Message</div>
    <div class="btn-submit">SUBMIT</div>
  </form>
</main>

<footer>
  <div class="abs footer-links">Home<span>|</span>Ketamine Description<span>|</span>About Us<span>|</span>The Ketamine Therapy<span>|</span>FAQ</div>
  <div class="abs copyright">Copyright&nbsp; ©&nbsp; 2015&nbsp; The Brightvale Clinic.&nbsp; All rights reserved.</div>
  <div class="abs social s1"></div>
  <div class="abs social s2"></div>
  <div class="abs social s3"></div>
</footer>

</body>
</html>
```